Wordpress Design for a Digital Management Consulting Business

I need a simple Wordpress Design and someone to set it up for a new boutique management consulting business called Tidewell Advisory that specialises in providing strategic advice to help grow digital businesses. It covers business strategy, marketing strategy, digital strategy, web product development, marketing campaigns, social, search, etc. From strategy to implementation.

URL is: tidewelladvisory.com.au

My professional background is here: au.examplenet.com/in/norabellweather

Competitors: other boutique digital/marketing management consulting businesses in Australia

The logos, colours and fonts are attached.

I would like the site to convey a business that is Smart/intelligent, Contemporary, Progressive, Digital, Energetic, Friendly.

The objective of the site is to educate visitors about what Tidewell Advisory does and encourage them to contact me for more information. It will be very light on content.

Target Market(s)

CEOs/Managing Directors, General Managers, Marketing Directors

Industry/Entity Type

Management Consulting

Font styles to use
Sans Serif

Colors
e34197
5c5c5c
000000

Requirements
Must have
• Site design requirements:
• Choose an appropriate Wordpress template, set it up for me and let me be able to edit it ongoing.
• It should use lots of images - these can be inspirational and not necessarily tied directly to the work
• Pink should feature, but not be the dominant colour.
• Site structure should be:
• 1. Home page - image led with horizontal navigation. Text beneath and images to describe the services.
• 2. About page - with space to write text and insert a picture of the Director
• 3. Services - with space to highlight services either as a list or graphically with text
• 4. Contact page - with space to write text and add email links, etc.
• Should have horizontal navigation
• It should have the flexibility to add another page
Nice to have
• Use the tree icon somehow in the design - consider in the background enlarged
• Use pink, grey, black from logo. Can introduce another complimentary colour if necessary.
• Can introduce another complimentary font to go with the logo font.
Should not have
• Use cliched business images and icons, eg. business suits, hand shakes, business men, business ties.

```html
<!DOCTYPE html>
<html lang="en">
<head>
<meta charset="utf-8">
<title>Tidewell Advisory</title>
<link href="https://fonts.googleapis.com/css2?family=Didact+Gothic&family=Questrial&display=swap" rel="stylesheet">
<style>
:root{
  --pink:#e34197;
  --grey:#5c5c5c;
  --black:#000000;
  --light:#f1f1f1;
  --line:#e2e2e2;
  --footer:#3a3a3a;
  --footer-text:#a9a9a9;
  --muted:#8a8a8a;
  --white:#ffffff;
}
*{box-sizing:border-box;margin:0;padding:0}
html,body{width:861px;height:1200px;overflow:hidden;background:var(--white)}
body{font-family:"Didact Gothic",sans-serif;color:var(--grey);font-size:8px;line-height:1.5}
.page{position:relative;width:861px;height:1200px;overflow:hidden}
.wrap{width:520px;margin:0 auto;position:relative}

/* header */
.site-header{height:40px;display:flex;align-items:center}
.site-header .wrap{display:flex;justify-content:space-between;align-items:center}
.brand{display:flex;align-items:center;gap:6px;font-family:"Questrial",sans-serif;font-size:13px;color:var(--pink);letter-spacing:.5px}
.brand-dot{width:10px;height:10px;border-radius:50%;background:var(--pink)}
.main-nav{display:flex;gap:4px}
.main-nav a{font-family:"Questrial",sans-serif;font-size:7px;color:var(--grey);text-decoration:none;padding:4px 9px;letter-spacing:.5px}
.main-nav a.current{border:1px solid var(--pink);color:var(--pink)}

/* hero */
.hero{position:relative;height:247px;overflow:hidden}
.hero-photo{position:absolute;inset:0;
  background:
    radial-gradient(ellipse 70px 40px at 330px 0px,#3b2a22 0%,#6a5448 45%,rgba(240,240,240,0) 100%),
    radial-gradient(ellipse 260px 170px at 690px 110px,#fbfbfb 0%,#e3e4e6 45%,rgba(205,206,209,0) 100%),
    linear-gradient(100deg,#f4f4f4 0%,#ececec 40%,#c8c9cc 70%,#a9abae 100%)}
.hero-inner{position:absolute;left:178px;top:60px;width:290px}
.hero-title{font-family:"Questrial",sans-serif;font-weight:400;font-size:34px;line-height:1.05;color:var(--pink);letter-spacing:1px}
.hero-text{margin-top:12px;font-size:7px;color:var(--grey)}
.btn-outline{display:inline-block;margin-top:12px;border:1px solid var(--grey);color:var(--grey);font-size:7px;padding:4px 12px;text-decoration:none}
.hero-dots{position:absolute;bottom:10px;left:50%;transform:translateX(-50%);display:flex;gap:5px}
.hero-dots span{width:5px;height:5px;border-radius:50%;background:#bdbdbd}
.hero-dots span.active{background:var(--pink)}
.hero-arrow{position:absolute;top:140px;left:158px;width:10px;height:16px}

/* sections */
.section{position:relative}
.section-services{height:288px;padding-top:45px}
.section-work{height:286px;padding-top:35px}
.section-title{font-family:"Questrial",sans-serif;font-weight:400;font-size:11px;color:var(--pink);letter-spacing:.5px;padding-bottom:4px;border-bottom:1px solid var(--line);display:block}
.section-title span{border-bottom:1px solid var(--pink);padding-bottom:4px}
.cards{display:flex;justify-content:space-between;padding:0 28px;margin-top:30px}
.card{width:120px;text-align:center}
.card-media{height:58px;width:100%}
.card-title{font-family:"Questrial",sans-serif;font-weight:400;font-size:7px;color:var(--grey);margin-top:10px;letter-spacing:.4px;min-height:18px;line-height:1.3}
.card-text{font-size:6.5px;color:var(--muted);line-height:1.45;text-align:left;padding:0 8px;min-height:30px}
.btn-pink{display:inline-block;margin-top:8px;background:var(--pink);color:var(--white);font-size:6.5px;padding:4px 14px;text-decoration:none}
.divider{position:absolute;left:0;right:0;bottom:0;border:0;border-top:1px solid var(--line)}

/* image tones */
.tone-laptop{background:linear-gradient(135deg,#23302f 0%,#4f5d5e 45%,#b9c2c4 100%)}
.tone-devices{background:radial-gradient(ellipse at 50% 55%,#3c3c3c 0%,#8d8d8d 30%,#f4f4f4 75%)}
.tone-network{background:radial-gradient(ellipse at 60% 40%,#bfe2ff 0%,#3e86c6 40%,#0b2f5c 100%)}
.tone-sketch{background:linear-gradient(135deg,#fafbfc 0%,#d9e4ee 50%,#7fa1bf 100%)}
.tone-charts{background:linear-gradient(135deg,#e6eef4 0%,#7e9cb6 55%,#35536e 100%)}
.tone-team{background:linear-gradient(120deg,#f2e4da 0%,#c7a28c 45%,#6f8fb0 100%)}

/* about */
.about{background:var(--light);height:224px;padding-top:40px}
.about .wrap{display:flex;gap:48px}
.director{width:116px;text-align:center;margin-left:10px}
.director-photo{width:116px;height:116px;border-radius:50%;background:radial-gradient(circle at 50% 38%,#f1d9b8 0%,#d6a878 35%,#7b6a5e 75%,#4b4b4b 100%)}
.director-name{font-family:"Questrial",sans-serif;font-size:7px;color:var(--pink);margin-top:8px;letter-spacing:.4px}
.director-role{font-size:6.5px;color:var(--grey)}
.about-body{flex:1;padding-top:-4px}
.about-title{font-family:"Questrial",sans-serif;font-size:13px;color:var(--pink);font-weight:400;letter-spacing:.5px;margin-bottom:8px}
.about-body p{font-size:7px;color:var(--grey);margin-bottom:8px}

/* footer */
.site-footer{position:relative;background:var(--footer);height:115px;padding-top:16px;color:var(--footer-text)}
.footer-row{display:flex;justify-content:space-between;align-items:flex-start}
.footer-col{font-size:6px;line-height:1.6}
.footer-col h4{font-family:"Questrial",sans-serif;font-weight:400;font-size:6.5px;color:var(--white);margin-bottom:3px}
.footer-map{width:70px;height:40px;margin-top:10px;background:linear-gradient(135deg,#eeeee8,#cfd8c6)}
.social{display:flex;gap:3px;margin-top:10px}
.social span{width:8px;height:8px}
.footer-brand{font-family:"Questrial",sans-serif;font-size:11px;color:var(--muted);display:flex;align-items:center;gap:5px;margin-top:14px}
.footer-brand i{width:9px;height:9px;border-radius:50%;background:var(--muted);display:block}
.copyright{position:absolute;left:0;right:0;bottom:6px;text-align:center;font-size:5.5px;color:var(--muted)}
</style>
</head>
<body>
<div class="page">

  <header class="site-header">
    <div class="wrap">
      <div class="brand"><span class="brand-dot"></span>Tidewell Advisory</div>
      <nav class="main-nav">
        <a href="#" class="current">HOME</a>
        <a href="#">SERVICES</a>
        <a href="#">WHAT WE DO</a>
        <a href="#">ABOUT</a>
        <a href="#">CONTACT</a>
      </nav>
    </div>
  </header>

  <section class="hero">
    <div class="hero-photo" role="img" aria-label="Bright desk with an open silver laptop and a cup of coffee"></div>
    <svg class="hero-arrow" viewBox="0 0 10 16"><polyline points="8,2 2,8 8,14" fill="none" stroke="#9a9a9a" stroke-width="1.5"/></svg>
    <div class="hero-inner">
      <h1 class="hero-title">TIDEWELL<br>ADVISORY</h1>
      <p class="hero-text">Tidewell Advisory helps growing digital businesses turn clear strategy into practical action, from first planning session to launch and ongoing growth across every channel.</p>
      <a href="#" class="btn-outline">Read more</a>
    </div>
    <div class="hero-dots"><span class="active"></span><span></span><span></span></div>
  </section>

  <section class="section section-services">
    <div class="wrap" style="height:100%">
      <h2 class="section-title"><span>SERVICES</span></h2>
      <div class="cards">
        <article class="card">
          <div class="card-media tone-laptop" role="img" aria-label="Hands typing on a laptop"></div>
          <h3 class="card-title">DIGITAL STRATEGY</h3>
          <p class="card-text">Clear plans that align your team, budget and goals with the digital market you want to win.</p>
          <a href="#" class="btn-pink">Read more</a>
        </article>
        <article class="card">
          <div class="card-media tone-devices" role="img" aria-label="Website shown on desktop, tablet and phone screens"></div>
          <h3 class="card-title">MARKETING STRATEGY</h3>
          <p class="card-text">Campaigns built on real customer insight, tested quickly and measured well so every dollar works.</p>
          <a href="#" class="btn-pink">Read more</a>
        </article>
        <article class="card">
          <div class="card-media tone-network" role="img" aria-label="Glowing blue digital network"></div>
          <h3 class="card-title">WEB PRODUCT DEVELOPMENT</h3>
          <p class="card-text">From early concept to launch, we guide product choices so your site and apps serve users.</p>
          <a href="#" class="btn-pink">Read more</a>
        </article>
      </div>
      <hr class="divider">
    </div>
  </section>

  <section class="section section-work">
    <div class="wrap">
      <h2 class="section-title"><span>WHAT WE DO</span></h2>
      <div class="cards">
        <article class="card">
          <div class="card-media tone-sketch" role="img" aria-label="Hands sketching ideas on paper"></div>
          <h3 class="card-title">STRATEGIC THINKING</h3>
          <p class="card-text">We step back, ask the hard questions and shape a direction your whole business can follow.</p>
          <a href="#" class="btn-pink">Read more</a>
        </article>
        <article class="card">
          <div class="card-media tone-charts" role="img" aria-label="Charts and reports spread on a desk"></div>
          <h3 class="card-title">ANALYTICAL APPROACH</h3>
          <p class="card-text">Decisions rest on data, search trends and audience research rather than guesswork.</p>
          <a href="#" class="btn-pink">Read more</a>
        </article>
        <article class="card">
          <div class="card-media tone-team" role="img" aria-label="Colleagues reviewing a project together"></div>
          <h3 class="card-title">PRACTICAL PROJECT MANAGEMENT</h3>
          <p class="card-text">Plans become delivery with steady timelines and honest reporting.</p>
          <a href="#" class="btn-pink">Read more</a>
        </article>
      </div>
    </div>
  </section>

  <section class="about">
    <div class="wrap">
      <div class="director">
        <div class="director-photo" role="img" aria-label="Portrait photo of the director"></div>
        <div class="director-name">NORA BELLWEATHER</div>
        <div class="director-role">Director</div>
      </div>
      <div class="about-body">
        <h2 class="about-title">ABOUT NORA</h2>
        <p>Nora founded Tidewell Advisory after many years leading digital and marketing teams, helping brands find new customers and grow revenue through smart online strategy and steady execution.</p>
        <p>Her experience spans business planning, product launches, search, social and campaign work for companies ranging from new ventures to established national organisations across Australia.</p>
        <p>She works closely with leaders to set clear priorities, build capable teams and deliver results.</p>
      </div>
    </div>
  </section>

  <footer class="site-footer">
    <div class="wrap footer-row">
      <div class="footer-col">
        <h4>Contact</h4>
        Phone 02 5550 1842<br>
        hello@tidewelladvisory.com.au
      </div>
      <div class="footer-col">
        <h4>Address</h4>
        Level 4, 18 Harbour Lane<br>
        Sydney NSW 2000
      </div>
      <div class="footer-map" role="img" aria-label="Street map of the office location"></div>
      <div class="social">
        <span style="background:#5a7bbf"></span>
        <span style="background:#6fbde8"></span>
        <span style="background:#3c8fc4"></span>
        <span style="background:#d9574a"></span>
      </div>
      <div class="footer-brand"><i></i>Tidewell Advisory</div>
    </div>
    <p class="copyright">© 2024 Tidewell Advisory. All rights reserved.</p>
  </footer>

</div>
</body>
</html>
```